Kestwell Finanz AG needs web design

We need a website for a Swiss company: Kestwell Finanz AG. We offer our customers financial services such as advice and funds. We also have an interest rate calculator that we want to link to via a button on the website.

We are looking for a black and gold design. (Background: Black, Accents: Gold and White)
The design should convey security and growth. We have uploaded our logo in the attachment.
Font from the logo: Trajan Pro Regular

```html
<!DOCTYPE html>
<html lang="en">
<head>
<meta charset="utf-8">
<title>Kestwell Finanz AG</title>
<link rel="stylesheet" href="https://fonts.googleapis.com/css2?family=Cinzel:wght@400;600&family=Lato:wght@400;700&display=swap">
<style>
:root{
  --black:#060606;
  --panel:#0f0f0f;
  --gold:#c9a45c;
  --gold-light:#ecd69a;
  --gold-dark:#8c6a2e;
  --white:#ffffff;
  --text:#d8d2c4;
  --grad-gold:linear-gradient(180deg,#f3dfa4 0%,#c9a45c 45%,#9a7636 100%);
}
*{box-sizing:border-box;margin:0;padding:0}
html,body{width:1200px;height:4079px;overflow:hidden;background:var(--black)}
body{position:relative;font-family:'Lato',Arial,sans-serif;color:var(--text)}
.abs{position:absolute}
.serif{font-family:'Cinzel',Georgia,serif}

/* header */
.topbar{position:absolute;top:0;left:0;width:1200px;height:65px;background:var(--black)}
.topbar .item{position:absolute;top:24px;font-size:12px;color:var(--gold);display:flex;align-items:center;gap:7px}
.social{position:absolute;width:34px;height:34px;border:1.5px solid var(--gold);border-radius:50%}
.navband{position:absolute;top:65px;left:0;width:1200px;height:59px;background:var(--grad-gold)}
.navband a{position:absolute;top:22px;font-size:12px;font-weight:700;color:#2a1e0a;text-decoration:none;letter-spacing:.2px}
.brand-seal{position:absolute;left:524px;top:11px;width:152px;height:152px;border-radius:50%;background:var(--black);border:3px solid var(--gold);box-shadow:0 0 0 4px #000;display:flex;align-items:center;justify-content:center;text-align:center;z-index:3}
.brand-seal span{font-family:'Cinzel',Georgia,serif;color:var(--gold);font-size:15px;line-height:20px;width:110px}

/* hero */
.hero{position:absolute;top:124px;left:0;width:1200px;height:621px;background:radial-gradient(ellipse at 50% 30%,#a07a4a 0%,#4a4f5a 30%,#242a34 60%,#0d1015 100%);text-align:center}
.hero .welcome{position:absolute;top:182px;left:0;width:100%;font-family:'Cinzel',Georgia,serif;font-size:31px;color:var(--white)}
.hero h1{position:absolute;top:222px;left:0;width:100%;font-family:'Cinzel',Georgia,serif;font-weight:400;font-size:76px;line-height:90px;color:var(--white)}
.hero p{position:absolute;top:322px;left:170px;width:860px;font-size:12.5px;line-height:24px;color:var(--white)}
.btn-gold{position:absolute;height:52px;border-radius:26px;background:var(--grad-gold);color:#2a1e0a;font-family:'Cinzel',Georgia,serif;font-size:15px;display:flex;align-items:center;justify-content:center;text-decoration:none}
.btn-outline{position:absolute;height:52px;border-radius:26px;border:2px solid var(--gold);color:var(--gold);font-family:'Cinzel',Georgia,serif;font-size:15px;display:flex;align-items:center;justify-content:center}

/* gold band */
.band{position:absolute;left:0;width:1200px;height:32px;z-index:2}
.scroll-down{position:absolute;left:568px;top:728px;width:64px;height:64px;border-radius:50%;background:#111;z-index:3;display:flex;align-items:center;justify-content:center}

/* sections */
.section{position:absolute;left:0;width:1200px}
.section-head{position:absolute;left:0;width:100%;text-align:center;font-family:'Cinzel',Georgia,serif;font-weight:400}
.section-head .kicker{display:flex;align-items:center;justify-content:center;gap:22px;font-size:40px;line-height:46px;color:var(--white)}
.section-head .kicker::before,.section-head .kicker::after{content:"";width:126px;height:4px;background:linear-gradient(90deg,transparent,var(--gold) 30%,var(--gold-light) 60%,var(--gold))}
.section-head .title{display:block;font-size:40px;line-height:46px;color:var(--gold)}
.intro{position:absolute;left:205px;width:790px;text-align:center;font-size:12.5px;line-height:24px;color:var(--white)}
.photo{position:absolute}

/* about */
.about{top:775px;height:737px;background:var(--black)}
.about .copy{position:absolute;left:597px;top:286px;width:468px;font-size:12px;line-height:24px;text-align:justify;color:var(--white)}

/* services */
.services{top:1543px;height:689px;background:linear-gradient(180deg,#0b0b0b,#151515 50%,#0a0a0a)}
.service{position:absolute;top:238px;width:222px;height:388px;border-radius:111px;background:linear-gradient(180deg,#1c1c1c,#0c0c0c);text-align:center}
.service .pic{position:absolute;left:13px;top:8px;width:196px;height:196px;border-radius:50%;border:2px solid var(--gold)}
.service .badge{position:absolute;left:81px;top:173px;width:60px;height:60px;border-radius:50%;background:var(--grad-gold);display:flex;align-items:center;justify-content:center}
.service h3{position:absolute;top:253px;width:100%;font-family:'Cinzel',Georgia,serif;font-weight:400;font-size:15px;color:var(--white)}
.service p{position:absolute;top:281px;width:100%;font-size:12px;line-height:25px;color:var(--text)}
.service .arrow{position:absolute;left:97px;top:346px}

/* testimonials */
.testimonials{top:2264px;height:538px;background:var(--black)}
.avatar{position:absolute;width:164px;height:164px;border-radius:50%;background:radial-gradient(circle at 50% 40%,#c8b9a8,#6b5e52 70%,#3a332c)}
.quote{position:absolute;top:269px;width:272px;font-size:12px;line-height:24px;color:var(--white)}
.name{position:absolute;top:426px;font-family:'Cinzel',Georgia,serif;font-size:17px;color:var(--gold)}
.stars{position:absolute;top:427px;color:var(--gold);font-size:17px;letter-spacing:2px}

/* blog */
.blog{top:2802px;height:855px;background:linear-gradient(180deg,#050505,#161616 60%,#0a0a0a)}
.post-title{position:absolute;font-family:'Cinzel',Georgia,serif;font-size:15px;line-height:28px;color:var(--white);letter-spacing:.5px}
.post-text{position:absolute;font-size:12px;line-height:24px;color:var(--white)}
.read-more{position:absolute;left:144px;top:726px;font-family:'Cinzel',Georgia,serif;font-size:14px;color:var(--gold);text-decoration:underline}

/* footer */
.footer{top:3689px;height:390px;background:#0c0c0c}
.footer h4{position:absolute;top:58px;font-family:'Cinzel',Georgia,serif;font-weight:400;font-size:17px;color:var(--white);letter-spacing:.5px}
.quick-links{position:absolute;left:326px;top:92px;list-style:none}
.quick-links li{height:28px;font-size:13px;color:var(--white)}
.quick-links li::before{content:"»";color:var(--white);margin-right:14px}
.contact-row{position:absolute;left:534px;display:flex;gap:16px;font-size:13px;line-height:28px;color:var(--white)}
.contact-row .ic{width:30px;height:30px;border-radius:50%;background:var(--grad-gold);display:flex;align-items:center;justify-content:center;flex:none;margin-top:0}
.field{position:absolute;background:var(--white);border:1px solid #bbb;font-size:11px;color:#444;padding:8px}
.footer-brand{position:absolute;left:66px;top:140px;width:220px;text-align:center;font-family:'Cinzel',Georgia,serif;font-size:20px;color:var(--gold)}
.divider{position:absolute;left:48px;top:310px;width:1104px;height:1px;background:#555}
.copyright{position:absolute;top:338px;left:0;width:100%;text-align:center;font-size:11px;color:var(--white)}
</style>
</head>
<body>

<header>
  <div class="topbar">
    <div class="item" style="left:133px">
      <svg width="11" height="11" viewBox="0 0 24 24"><path fill="#c9a45c" d="M6.6 10.8a15 15 0 0 0 6.6 6.6l2.2-2.2c.3-.3.7-.4 1-.2 1.1.4 2.3.6 3.6.6.6 0 1 .4 1 1V20c0 .6-.4 1-1 1C10.6 21 3 13.4 3 4c0-.6.4-1 1-1h3.5c.6 0 1 .4 1 1 0 1.3.2 2.5.6 3.6.1.3 0 .7-.2 1z"/></svg>
      +41 44 555 0182
    </div>
    <div class="item" style="left:310px">
      <svg width="12" height="10" viewBox="0 0 24 18"><rect width="24" height="18" rx="2" fill="#c9a45c"/><path d="M1 2l11 8 11-8" stroke="#060606" stroke-width="2" fill="none"/></svg>
      info@kestwellfinanz.ch
    </div>
    <div class="item" style="left:733px;font-style:italic">
      <svg width="11" height="11" viewBox="0 0 24 24"><circle cx="10" cy="10" r="7" stroke="#c9a45c" stroke-width="3" fill="none"/><path d="M15 15l7 7" stroke="#c9a45c" stroke-width="3"/></svg>
      Search
    </div>
    <span class="social" style="left:893px;top:15px" aria-label="Social link"></span>
    <span class="social" style="left:939px;top:15px" aria-label="Social link"></span>
    <span class="social" style="left:987px;top:15px" aria-label="Social link"></span>
    <span class="social" style="left:1033px;top:15px" aria-label="Social link"></span>
  </div>
  <nav class="navband">
    <a href="#" style="left:131px">HOME</a>
    <a href="#" style="left:198px">ABOUT US</a>
    <a href="#" style="left:288px">INVESTMENT APPROACH</a>
    <a href="#" style="left:763px">PORTFOLIO</a>
    <a href="#" style="left:862px">BLOG</a>
    <a href="#" style="left:922px">REVIEWS</a>
    <a href="#" style="left:1005px">CONTACT</a>
  </nav>
  <div class="brand-seal"><span>KESTWELL FINANZ AG</span></div>
</header>

<section class="hero" role="img" aria-label="Businessman climbing a staircase toward a city skyline with rising arrows">
  <div class="welcome">WELCOME TO</div>
  <h1>KESTWELL FINANZ</h1>
  <p>Lorem ipsum dolor sit amet, consectetur adipiscing elit, sed do eiusmod tempor incididunt ut labore et dolore magna aliqua. Ut enim ad minim veniam, quis nostrud exercitation ullamco laboris nisi ut aliquip ex ea commodo consequat.</p>
  <a class="btn-gold" href="#" style="left:457px;top:390px;width:286px">INTEREST RATE CALCULATOR</a>
</section>

<svg class="band" style="top:745px" viewBox="0 0 1200 32" preserveAspectRatio="none" aria-hidden="true">
  <defs><linearGradient id="bandGold" x1="0" x2="0" y1="0" y2="1"><stop offset="0" stop-color="#f3dfa4"/><stop offset=".5" stop-color="#c9a45c"/><stop offset="1" stop-color="#8c6a2e"/></linearGradient></defs>
  <path d="M0 0 Q600 26 1200 0 L1200 32 Q600 10 0 32Z" fill="url(#bandGold)"/>
</svg>
<div class="scroll-down"><svg width="22" height="20" viewBox="0 0 22 20"><path d="M3 2l8 7 8-7M3 10l8 7 8-7" stroke="#c9a45c" stroke-width="2" fill="none"/></svg></div>

<section class="section about">
  <h2 class="section-head" style="top:84px"><span class="kicker">ABOUT</span><span class="title">KESTWELL FINANZ</span></h2>
  <p class="intro" style="top:192px">Lorem ipsum dolor sit amet, consectetur adipiscing elit, sed do eiusmod tempor incididunt ut labore et dolore magna aliqua. Ut enim ad minim veniam, quis nostrud exercitation ullamco laboris nisi ut aliquip ex ea commodo consequat.</p>
  <div class="photo" role="img" aria-label="Hands framing a glowing rising bar chart on a tablet" style="left:143px;top:254px;width:386px;height:386px;border-radius:50%;border:2px solid var(--gold);background:radial-gradient(circle at 50% 55%,#7a4a2a 0%,#2c1c14 45%,#0a0a0a 80%)"></div>
  <p class="copy">Lorem ipsum dolor sit amet, consectetur adipiscing elit, sed do eiusmod tempor incididunt ut labore et dolore magna aliqua. Ut enim ad minim veniam, quis nostrud exercitation ullamco laboris nisi ut aliquip ex ea commodo consequat. Duis aute irure dolor in reprehenderit in voluptate velit esse cillum dolore eu fugiat nulla pariatur. Excepteur sint occaecat cupidatat non proident, sunt in culpa qui officia deserunt mollit anim id est laborum Sed ut perspiciatis unde omnis iste natus error sit voluptatem accusantium doloremque laudantium, totam rem aperiam, eaque ipsa quae ab illo inventore veritatis et quasi architecto beatae vitae dicta sunt explicabo. Nemo enim ipsam voluptatem quia voluptas sit aspernatur aut odit aut fugit, sed quia consequuntur magni dolores eos qui ratione voluptatem sequi nesciunt. Neque porro quisquam est, qui dolorem ipsum quia dolor sit amet.</p>
  <div class="btn-outline" style="left:597px;top:567px;width:288px">INTEREST RATE CALCULATOR</div>
</section>

<svg class="band" style="top:1512px" viewBox="0 0 1200 32" preserveAspectRatio="none" aria-hidden="true"><path d="M0 0 Q600 26 1200 0 L1200 32 Q600 10 0 32Z" fill="url(#bandGold)"/></svg>

<section class="section services">
  <h2 class="section-head" style="top:56px"><span class="kicker">OUR</span><span class="title">SERVICES</span></h2>
  <p class="intro" style="top:163px">Lorem ipsum dolor sit amet, consectetur adipiscing elit, sed do eiusmod tempor incididunt ut labore et dolore magna aliqua. Ut enim ad minim veniam, quis nostrud exercitation ullamco laboris nisi ut aliquip ex ea commodo consequat.</p>

  <article class="service" style="left:187px">
    <div class="pic" role="img" aria-label="Small house model beside a laptop" style="background:radial-gradient(circle,#8fa6b8,#3c5468 70%,#1e2a36)"></div>
    <div class="badge"><svg width="24" height="22" viewBox="0 0 24 22"><rect x="2" y="2" width="20" height="18" rx="2" fill="none" stroke="#fff" stroke-width="2"/><path d="M6 8h12M6 12h12M6 16h8" stroke="#fff" stroke-width="2"/></svg></div>
    <h3>REAL ESTATE</h3>
    <p>debitis aut rerum nece ssitatib<br>saepe eveniet voluptates</p>
    <svg class="arrow" width="28" height="12" viewBox="0 0 28 12"><path d="M0 6h26M21 1l5 5-5 5" stroke="#fff" stroke-width="1.5" fill="none"/></svg>
  </article>

  <article class="service" style="left:483px">
    <div class="pic" role="img" aria-label="Advisor meeting with clients at a desk" style="background:radial-gradient(circle,#c9c4bc,#6e6a66 70%,#2a2a2c)"></div>
    <div class="badge"><svg width="24" height="22" viewBox="0 0 24 22"><rect x="2" y="2" width="20" height="18" rx="2" fill="none" stroke="#fff" stroke-width="2"/><path d="M6 8h12M6 12h12M6 16h8" stroke="#fff" stroke-width="2"/></svg></div>
    <h3>CONSUMER FINANCE</h3>
    <p>debitis aut rerum nece ssitatib<br>saepe eveniet voluptates</p>
    <svg class="arrow" width="28" height="12" viewBox="0 0 28 12"><path d="M0 6h26M21 1l5 5-5 5" stroke="#fff" stroke-width="1.5" fill="none"/></svg>
  </article>

  <article class="service" style="left:779px">
    <div class="pic" role="img" aria-label="Hand holding an umbrella over a glowing family icon" style="background:radial-gradient(circle,#5aa0d8,#1f4a78 60%,#101822)"></div>
    <div class="badge"><svg width="24" height="22" viewBox="0 0 24 22"><rect x="2" y="2" width="20" height="18" rx="2" fill="none" stroke="#fff" stroke-width="2"/><path d="M6 8h12M6 12h12M6 16h8" stroke="#fff" stroke-width="2"/></svg></div>
    <h3>INSURANCE</h3>
    <p>debitis aut rerum nece ssitatib<br>saepe eveniet voluptates</p>
    <svg class="arrow" width="28" height="12" viewBox="0 0 28 12"><path d="M0 6h26M21 1l5 5-5 5" stroke="#fff" stroke-width="1.5" fill="none"/></svg>
  </article>
</section>

<svg class="band" style="top:2232px" viewBox="0 0 1200 32" preserveAspectRatio="none" aria-hidden="true"><path d="M0 0 Q600 26 1200 0 L1200 32 Q600 10 0 32Z" fill="url(#bandGold)"/></svg>

<section class="section testimonials">
  <h2 class="section-head" style="top:75px"><span class="kicker">OUR</span><span class="title">CLIENT TESTIMONIALS</span></h2>
  <p class="intro" style="top:182px">Lorem ipsum dolor sit amet, consectetur adipiscing elit, sed do eiusmod tempor incididunt ut labore et dolore magna aliqua. Ut enim ad minim veniam, quis nostrud exercitation ullamco laboris nisi ut aliquip ex ea commodo consequat.</p>

  <div class="avatar" role="img" aria-label="Portrait of client Nora" style="left:140px;top:255px"></div>
  <p class="quote" style="left:325px">Lorem ipsum dolor sit amet, consectetur adipiscing elit, sed do eiusmod tempor incididunt ut labore et dolore magna aliqua. Ut enim ad minim veniam, quis nostrud exercitation ullamco laboris nisi ut aliquip ex ea commodo consequat. Duis aute irure dolor in reprehenderit.</p>
  <div class="name" style="left:327px">NORA</div>
  <div class="stars" style="left:470px">★★★★★</div>

  <p class="quote" style="left:620px">Lorem ipsum dolor sit amet, consectetur adipiscing elit, sed do eiusmod tempor incididunt ut labore et dolore magna aliqua. Ut enim ad minim veniam, quis nostrud exercitation ullamco laboris nisi ut aliquip ex ea commodo consequat. Duis aute irure dolor in reprehenderit.</p>
  <div class="name" style="left:615px">JONAS REBER</div>
  <div class="stars" style="left:790px">★★★★★</div>
  <div class="avatar" role="img" aria-label="Portrait of client Jonas Reber" style="left:896px;top:255px"></div>
</section>

<section class="section blog">
  <h2 class="section-head" style="top:77px"><span class="kicker">OUR</span><span class="title">LATEST BLOG</span></h2>
  <p class="intro" style="top:185px">Lorem ipsum dolor sit amet, consectetur adipiscing elit, sed do eiusmod tempor incididunt ut labore et dolore magna aliqua. Ut enim ad minim veniam, quis nostrud exercitation ullamco laboris nisi ut aliquip ex ea commodo consequat.</p>

  <div class="photo" role="img" aria-label="Businessman watering a growing plant on stacks of gold coins" style="left:138px;top:269px;width:446px;height:285px;background:linear-gradient(135deg,#1c2c52 0%,#0f1a34 55%,#6a4a1e 100%)"></div>
  <div class="post-title" style="left:144px;top:585px;width:430px">LOREM IPSUM DOLOR SIT AMET, CONSECTETUR ADIPISCING ELIT SED DO EIUSMOD.</div>
  <p class="post-text" style="left:144px;top:647px;width:430px;font-size:13px">Lorem ipsum dolor sit amet, consectetur adipiscing elit, sed do eiusmod tempor incididunt ut labore et dolore magna aliqua. Ut enim ad minim veniam quis nostrud exercitation.</p>
  <div class="read-more">READ MORE</div>

  <div class="photo" role="img" aria-label="Hand over a glowing financial chart" style="left:595px;top:269px;width:170px;height:159px;background:linear-gradient(135deg,#1e3c66,#0c1a30)"></div>
  <div class="post-title" style="left:784px;top:271px;width:300px">LOREM IPSUM DOLOR SIT AMET CONSECTETUR ADIPISCING.</div>
  <p class="post-text" style="left:784px;top:333px;width:250px">Lorem ipsum dolor sit amet, consectetur adipiscing elit, sed do eiusmod tempor incididunt ut labore et dolore.</p>

  <div class="photo" role="img" aria-label="Hands reviewing financial documents with a calculator" style="left:595px;top:442px;width:170px;height:159px;background:linear-gradient(135deg,#d8dde4,#7c8490)"></div>
  <div class="post-title" style="left:784px;top:443px;width:300px">LOREM IPSUM DOLOR SIT AMET CONSECTETUR ADIPISCING.</div>
  <p class="post-text" style="left:784px;top:500px;width:250px">Lorem ipsum dolor sit amet, consectetur adipiscing elit, sed do eiusmod tempor incididunt ut labore et dolore.</p>

  <div class="photo" role="img" aria-label="Business people discussing at a glass board" style="left:595px;top:614px;width:170px;height:159px;background:linear-gradient(135deg,#9a8aa8,#4a4058)"></div>
  <div class="post-title" style="left:784px;top:616px;width:300px">LOREM IPSUM DOLOR SIT AMET CONSECTETUR ADIPISCING.</div>
  <p class="post-text" style="left:784px;top:678px;width:250px">Lorem ipsum dolor sit amet, consectetur adipiscing elit, sed do eiusmod tempor incididunt ut labore et dolore.</p>
</section>

<svg class="band" style="top:3657px" viewBox="0 0 1200 32" preserveAspectRatio="none" aria-hidden="true"><path d="M0 0 Q600 26 1200 0 L1200 32 Q600 10 0 32Z" fill="url(#bandGold)"/></svg>

<footer class="section footer">
  <div class="footer-brand">KESTWELL FINANZ AG</div>
  <span class="social" style="left:91px;top:232px;background:var(--gold)" aria-label="Social link"></span>
  <span class="social" style="left:138px;top:232px;background:var(--gold)" aria-label="Social link"></span>
  <span class="social" style="left:185px;top:232px;background:var(--gold)" aria-label="Social link"></span>
  <span class="social" style="left:232px;top:232px;background:var(--gold)" aria-label="Social link"></span>

  <h4 style="left:326px">QUICK LINKS</h4>
  <ul class="quick-links">
    <li>Home</li><li>About Us</li><li>Investment Approach</li><li>Portfolio</li><li>Blog</li><li>Reviews</li><li>Contact</li>
  </ul>

  <h4 style="left:508px">CONTACT INFO</h4>
  <div class="contact-row" style="top:96px;left:520px">
    <span class="ic"><svg width="12" height="14" viewBox="0 0 24 28"><path d="M12 0a10 10 0 0 0-10 10c0 8 10 18 10 18s10-10 10-18A10 10 0 0 0 12 0zm0 14a4 4 0 1 1 0-8 4 4 0 0 1 0 8z" fill="#fff"/></svg></span>
    <span>123 Lorem ipsum dolor<br>sit amet, consectetur<br>adipiscing elit,</span>
  </div>
  <div class="contact-row" style="top:180px;left:520px">
    <span class="ic"><svg width="13" height="13" viewBox="0 0 24 24"><path fill="#fff" d="M6.6 10.8a15 15 0 0 0 6.6 6.6l2.2-2.2c.3-.3.7-.4 1-.2 1.1.4 2.3.6 3.6.6.6 0 1 .4 1 1V20c0 .6-.4 1-1 1C10.6 21 3 13.4 3 4c0-.6.4-1 1-1h3.5c.6 0 1 .4 1 1 0 1.3.2 2.5.6 3.6.1.3 0 .7-.2 1z"/></svg></span>
    <span>+41 44 555 0182</span>
  </div>
  <div class="contact-row" style="top:228px;left:520px">
    <span class="ic"><svg width="13" height="10" viewBox="0 0 24 18"><rect width="24" height="18" rx="2" fill="#fff"/><path d="M1 2l11 8 11-8" stroke="#c9a45c" stroke-width="2" fill="none"/></svg></span>
    <span>info@kestwellfinanz.ch</span>
  </div>

  <h4 style="left:760px;top:56px">CONTACT US</h4>
  <div class="field" style="left:757px;top:96px;width:170px;height:37px">First Name</div>
  <div class="field" style="left:932px;top:96px;width:168px;height:37px">Last Name</div>
  <div class="field" style="left:757px;top:140px;width:343px;height:37px">Email Address</div>
  <div class="field" style="left:757px;top:183px;width:343px;height:90px">Enquiry</div>
  <svg class="abs" style="left:1030px;top:203px" width="70" height="70" viewBox="0 0 70 70" aria-hidden="true">
    <path d="M70 0V70H0Z" fill="#b38d48"/>
    <path d="M40 56l20-14-6 20-4-6z" fill="#fff"/>
  </svg>

  <div class="divider"></div>
  <p class="copyright">© Copyright 2022 Kestwell Finanz AG. All rights reserved | Privacy Statement</p>
</footer>

</body>
</html>
```